Task and Project Management Tool Website

We need designs for both desktop and mobile for a new site, which is the marketing presentation of our new platform called Lanternfield, which is a task and project tool specific for the property sector. The name refers to people working on different workstreams on a property and crossing their paths when collaborating. The site will not do ecommerce, just a presentation of the product. We would like to include a video (no voice over) and some graphics, which we will do separately. The whole site will include a few pages, as detailed in the attach document. The product appeals to property companies and banks, hence the brand should portray reliability, corporate. We would like to see combinations of black, white and blue.
Updates

This project is currently put on hold. Client will be focusing on getting a Logo design first. Then once the logo has been created, we will resume this project and use the logo on the web designs submissions. Regards, QT Admin Barnaby

Logo design has been completed. Please resubmit and submit new web designs on this project using the logo design attached. Regards, QT Admin Barnaby

Target Market(s)

Corporate (B2B)

Logo Text

Lanternfield

Coding

Coded - Design and coding required

Number of Pages Required

5+ page

Requirements
Must have
• As in the specs
Should not have
• pictures of fake people (we prefer icons)

```html
<!DOCTYPE html>
<html lang="en">
<head>
<meta charset="utf-8">
<title>Lanternfield — Choice Way</title>
<link rel="stylesheet" href="https://fonts.googleapis.com/css2?family=Bebas+Neue&family=Oswald:wght@500&family=Quicksand:wght@400;500&family=Lato:wght@700&display=swap">
<style>
  :root {
    --blue: #2287c8;
    --cream: #f2ede3;
    --ink: #141414;
    --white: #ffffff;
  }
  * { margin: 0; padding: 0; box-sizing: border-box; }
  html, body {
    width: 1200px;
    height: 985px;
    overflow: hidden;
    background: var(--white);
  }
  .page {
    position: relative;
    width: 1200px;
    height: 985px;
  }
  .site-header {
    position: absolute;
    top: 0; left: 0;
    width: 1200px;
    height: 138px;
  }
  .brand {
    position: absolute;
    left: 112px;
    top: 36px;
    display: flex;
    align-items: center;
    gap: 16px;
  }
  .brand-dot {
    width: 76px;
    height: 76px;
    border-radius: 50%;
    background: var(--blue);
  }
  .brand-name {
    font-family: "Oswald", sans-serif;
    font-weight: 500;
    font-size: 46px;
    letter-spacing: 1px;
    color: var(--ink);
    text-transform: uppercase;
    line-height: 1;
  }
  .menu-toggle {
    position: absolute;
    left: 1023px;
    top: 55px;
    width: 50px;
    height: 37px;
    display: flex;
    flex-direction: column;
    justify-content: space-between;
  }
  .menu-toggle span {
    display: block;
    height: 5px;
    background: var(--blue);
  }
  .hero {
    position: absolute;
    left: 2px;
    top: 138px;
    width: 1196px;
    height: 703px;
    background: var(--blue);
  }
  .hero-title {
    position: absolute;
    left: 116px;
    top: 112px;
    font-family: "Bebas Neue", sans-serif;
    font-weight: 400;
    font-size: 108px;
    line-height: 98px;
    color: var(--cream);
  }
  .hero-copy {
    position: absolute;
    left: 114px;
    top: 324px;
    font-family: "Quicksand", sans-serif;
    font-weight: 500;
    font-size: 16.5px;
    line-height: 22px;
    color: var(--cream);
  }
  .hero-copy p + p { margin-top: 7px; }
  .hero-button {
    position: absolute;
    left: 116px;
    top: 452px;
    width: 207px;
    height: 50px;
    background: var(--cream);
    color: var(--blue);
    font-family: "Quicksand", sans-serif;
    font-weight: 500;
    font-size: 19px;
    display: flex;
    align-items: center;
    justify-content: center;
    text-decoration: none;
  }
  .hero-illustration {
    position: absolute;
    left: 458px;
    top: 83px;
    width: 593px;
    height: 530px;
    background: linear-gradient(145deg, #2a8fd0 0%, #f3e6cc 50%, #1a1a1a 100%);
    opacity: 0.55;
  }
  .section-heading {
    position: absolute;
    top: 890px;
    left: 0;
    width: 1200px;
    text-align: center;
    font-family: "Lato", sans-serif;
    font-weight: 700;
    font-size: 35px;
    color: var(--blue);
  }
</style>
</head>
<body>
<div class="page">
  <header class="site-header">
    <div class="brand">
      <div class="brand-dot"></div>
      <span class="brand-name">Lanternfield</span>
    </div>
    <nav class="menu-toggle" aria-label="Menu">
      <span></span><span></span><span></span>
    </nav>
  </header>

  <section class="hero">
    <h1 class="hero-title">Choice<br>Way</h1>
    <div class="hero-copy">
      <p>Lorem ipsum dolor sit amet<br>Curabitur elit felis, faucibus<br>commodo dui.</p>
      <p>Cras aliquam tincidunt tellus</p>
    </div>
    <a class="hero-button" href="#">Learn more</a>
    <div class="hero-illustration" role="img" aria-label="Isometric illustration of a person at a fork where a path splits into two arrows labelled easy and hard, with question, heart and emoji icons"></div>
  </section>

  <h2 class="section-heading">Help you the better choice</h2>
</div>
</body>
</html>
```